Webbanner-Design für Tanzschule
Zielgruppe
Wir sind eine Tanzschule und benötigen einen werbebanner.
Aufgabenstellung
Hierfür benötigen wir eine Banner (Haeder): https://www.tanzkreisnord.de/page/3/
Es soll enthalten sein:
Logo: Ritmo del Alba
Angebot: Salsa, Bachata, Kizomba, Zouk, Lady- & Menstyle
Einstiegsmöglichkeiten Jederzeit
Gratis Schnupperstunde - es soll zum Klick animieren
Es soll dich zum Tanzen einladen und professionell wirken.
Die Bilder sind nur eine Idee.
https://www.ritmo-del-alba.de/
It should contain:
Offer: Salsa, Bachata, Kizomba, Zouk, Lady- & Menstyle
Join the courses every month
Free trial lesson - it should encourage you to click
It should invite you to dance and look professional!
The pictures are just an idea!

```html
<!DOCTYPE html>
<html lang="de">
<head>
<meta charset="utf-8">
<title>Ritmo del Alba – News</title>
<link href="https://fonts.googleapis.com/css2?family=Bebas+Neue&family=Satisfy&family=Open+Sans:wght@300;400;600;700&family=Fira+Sans:wght@500;600&family=Noto+Sans:wght@400;700&display=swap" rel="stylesheet">
<style>
  :root{
    --magenta:#a8206a;
    --teal:#0f8a94;
    --ink:#1d1d1d;
    --grey-ring:#e6e1e1;
    --rule:#e8e8e8;
    --bar:#f4f4f4;
    --muted:#8a8a8a;
    --link-blue:#1e6fd0;
    --accent-blue:#13aff0;
    --flyer-low:#cfd8e6;
  }
  *{box-sizing:border-box;margin:0;padding:0}
  html,body{width:929px;height:1200px;overflow:hidden;background:#fff;font-family:"Noto Sans",Verdana,sans-serif;color:var(--ink)}
  .page{position:relative;width:929px;height:1200px}
  .rule{position:absolute;left:0;width:929px;height:1px;background:var(--rule)}
  .hero{position:absolute;left:0;top:41px;width:929px;height:413px;display:block}

  .hero-script{font-family:"Satisfy",cursive;font-size:58px;fill:var(--teal)}
  .hero-caps{font-family:"Bebas Neue",sans-serif;fill:var(--ink)}
  .hero-cta{font-family:"Bebas Neue",sans-serif;font-size:50px;letter-spacing:1px;fill:#fff}
  .hero-name{font-family:"Open Sans",sans-serif;font-weight:300;font-size:60px;fill:var(--ink)}
  .hero-tagline{font-family:"Open Sans",sans-serif;font-weight:300;font-size:23px;fill:#666}
  .hero-bullet{fill:var(--teal)}

  .site-header{position:absolute;left:0;top:501px;width:929px;height:51px}
  .brand{position:absolute;left:57px;top:11px;display:flex;align-items:center;gap:8px;font-family:"Noto Sans",sans-serif;font-weight:700;font-size:20px;color:#e8a317}
  .brand-mark{width:14px;height:14px;background:#e8a317}
  .nav{position:absolute;right:45px;top:17px;display:flex;gap:15px;font-size:10px;letter-spacing:2px;color:#333}

  .title-bar{position:absolute;left:0;top:552px;width:929px;height:71px;background:var(--bar)}
  .title-bar h1{position:absolute;left:57px;top:22px;font-family:"Open Sans",sans-serif;font-weight:400;font-size:17px;color:#333}
  .crumbs{position:absolute;right:46px;top:29px;font-size:9px;color:#333;display:flex;gap:5px;align-items:center}
  .crumbs .sep{color:#bbb}

  .flyer{position:absolute;left:57px;top:658px;width:372px;height:519px;font-family:"Fira Sans",sans-serif;color:#111;
    background:linear-gradient(180deg,#e9c9d3 0%,#eef0f6 22%,#d8dcec 38%,#e9e3ea 42%,var(--flyer-low) 43%,var(--flyer-low) 100%)}
  .flyer-backdrop{position:absolute;left:0;top:0;width:372px;height:219px;background:linear-gradient(90deg,rgba(200,90,110,.28),rgba(255,255,255,0) 45%,rgba(120,140,200,.18));}
  .flyer-head{position:absolute;left:0;top:22px;width:372px;text-align:center;font-weight:600;font-size:25px;line-height:36px}
  .flyer-levels{position:absolute;left:0;top:144px;width:372px;text-align:center;font-weight:600;font-size:25px;line-height:36px}
  .flyer-levels sup{font-size:14px}
  .flyer-details{position:absolute;left:34px;top:257px;font-weight:500;font-size:13.6px;line-height:18.6px}
  .flyer-details a{color:var(--link-blue);text-decoration:underline}
  .flyer-greeting{position:absolute;left:34px;top:424px;font-weight:600;font-size:13.6px}
  .flyer-notes{position:absolute;left:34px;top:454px;font-weight:500;font-size:11.5px;line-height:17px;color:#333}

  .post{position:absolute;left:453px;top:658px;width:430px}
  .post-cat{font-size:8.5px;font-weight:700;letter-spacing:.6px;color:var(--accent-blue);margin-top:3px}
  .post-title{font-size:18px;font-weight:700;letter-spacing:.4px;margin-top:8px;color:#333}
  .post-excerpt{font-size:8.4px;line-height:14.5px;color:#444;margin-top:13px}
  .post-meta{border-top:1px solid var(--rule);margin-top:10px;padding-top:10px;display:flex;justify-content:space-between;font-size:7.6px;font-weight:700;letter-spacing:.6px;color:var(--muted)}
</style>
</head>
<body>
<div class="page">
  <div class="rule" style="top:41px"></div>

  <svg class="hero" viewBox="0 0 1350 600" preserveAspectRatio="none" aria-label="Werbebanner Ritmo del Alba">
    <defs>
      <linearGradient id="groupPhoto" x1="0" y1="0" x2="0" y2="1">
        <stop offset="0" stop-color="#bcd5ea"/>
        <stop offset=".45" stop-color="#9aa89a"/>
        <stop offset="1" stop-color="#8c877f"/>
      </linearGradient>
      <linearGradient id="coupleRoom" x1="0" y1="0" x2="1" y2="1">
        <stop offset="0" stop-color="#f3ece6"/>
        <stop offset=".6" stop-color="#d8c9bf"/>
        <stop offset="1" stop-color="#b7b2ae"/>
      </linearGradient>
      <clipPath id="bannerClip"><rect width="1350" height="600"/></clipPath>
    </defs>
    <rect width="1350" height="600" fill="#fff"/>
    <g clip-path="url(#bannerClip)">
      <circle cx="250" cy="340" r="395" fill="#a8206a"/>
      <circle cx="238" cy="352" r="378" fill="#e6e1e1"/>
      <g role="img" aria-label="Foto: Gruppe von Tanzpaaren im Freien vor einem Gebäude">
        <circle cx="230" cy="360" r="366" fill="url(#groupPhoto)"/>
      </g>
      <circle cx="668" cy="200" r="236" fill="#0f8a94"/>
      <circle cx="660" cy="196" r="222" fill="#e6e1e1"/>
      <g role="img" aria-label="Foto: tanzendes Paar in einem hellen Raum">
        <circle cx="660" cy="200" r="212" fill="url(#coupleRoom)"/>
      </g>
      <rect x="822" y="132" width="600" height="134" rx="67" fill="#fff"/>
      <rect x="832" y="140" width="600" height="118" rx="59" fill="#a8206a"/>
    </g>
    <text class="hero-script" x="1107" y="68" text-anchor="middle" textLength="356" lengthAdjust="spacingAndGlyphs">Einstiegsmöglichkeiten</text>
    <text class="hero-caps" x="1108" y="116" text-anchor="middle" font-size="36" letter-spacing="14">JEDERZEIT</text>
    <text class="hero-cta" x="1096" y="216" text-anchor="middle">GRATIS SCHNUPPERSTUNDE</text>
    <g class="hero-caps" font-size="31" letter-spacing="3">
      <circle class="hero-bullet" cx="919" cy="312" r="6"/><text x="936" y="323">SALSA</text>
      <circle class="hero-bullet" cx="1032" cy="312" r="6"/><text x="1049" y="323">BACHATA</text>
      <circle class="hero-bullet" cx="1176" cy="312" r="6"/><text x="1193" y="323">KIZOMBA</text>
      <circle class="hero-bullet" cx="919" cy="358" r="6"/><text x="936" y="369">ZOUK</text>
      <circle class="hero-bullet" cx="1020" cy="358" r="6"/><text x="1037" y="369">LADY- &amp; MENSTYLE</text>
    </g>
    <text class="hero-name" x="940" y="498" text-anchor="middle">Ritmo del Alba</text>
    <text class="hero-tagline" x="940" y="538" text-anchor="middle">Salsa · Bachata · Kizomba</text>
    <circle cx="1240" cy="490" r="28" fill="#a8206a"/>
  </svg>
  <div class="rule" style="top:454px"></div>

  <div class="rule" style="top:501px"></div>
  <header class="site-header">
    <div class="brand"><span class="brand-mark"></span>tanzkreisnord.de</div>
    <nav class="nav"><span>News</span><span>Fotos</span><span>Imprint</span><span>Privacy Policy</span></nav>
  </header>

  <div class="title-bar">
    <h1>News</h1>
    <div class="crumbs">
      <svg width="10" height="10" viewBox="0 0 10 10"><path d="M1 5 L5 1.5 L9 5 M2.3 4 V9 H7.7 V4" fill="none" stroke="#555" stroke-width="1"/></svg>
      <span class="sep">&gt;</span><span>News</span><span class="sep">&gt;</span><span>Page 3</span>
    </div>
  </div>

  <article class="flyer" role="img" aria-label="Kursplakat auf Hintergrund in Flaggenfarben">
    <div class="flyer-backdrop"></div>
    <div class="flyer-head">Neue Rueda-Kurse<br>mit Clara &amp; Jonas<br>ab Di 16. November 2021</div>
    <div class="flyer-levels">20 Uhr Fortgeschrittene<sup>1</sup><br>21 Uhr Einsteiger<sup>2</sup></div>
    <div class="flyer-details">
      Anzahl und Dauer Stunden: 8 x 45 min<br>
      Preis: 50 € pro Person und Kurs, 40 € ermäßigt<br>
      Anmeldung: <a>info@rueda-suedbaden.de</a><br>
      Max. Teilnehmeranzahl: 6 Paare<br>
      Corona-Regeln: 2G<br>
      Veranstalter: Rueda con Canela e.V.<br>
      Ort: Jugendtreff Am Mühlbach<br>
      Adresse: Lindenweg 4, 79106 Freiburg
    </div>
    <div class="flyer-greeting">Wir freuen uns auf euch!</div>
    <div class="flyer-notes"><sup>1</sup>Fortgeschritten = mind. 1 Jahr Rueda-Erfahrung<br><sup>2</sup>Einsteiger = mind. 1 Jahr Salsa-Erfahrung</div>
  </article>

  <article class="post">
    <div class="post-cat">CLASS</div>
    <h2 class="post-title">Neue Rueda-Kurse mit Clara &amp; Jonas</h2>
    <p class="post-excerpt">Neue Rueda-Kurse mit Clara &amp; Jonas ab Di 16. November 2021 20 Uhr Fortgeschrittene 21 Uhr Einsteiger Anzahl und Dauer Stunden: 8 x 45 min Preis: 50 € pro Person…</p>
    <div class="post-meta"><span>&#9675; COMMENTS OFF</span><span>OCTOBER 27, 2021</span></div>
  </article>

  <div class="rule" style="top:1197px;left:57px;width:826px"></div>
</div>
</body>
</html>
```